23rd Annual Harrowgate Lantern Film Festival Poster

Design an eye catchy, stylish poster for our 23rd film festival. Be different not just a poster with a film reel. Think outside of the box with a design that will attract peoples attention. Colorful (you choose the colors). Make it fun and creative, like the film festival. Show your talents in the design. Be sure it is new and stylish. Dates are August 21 - 29, 2020. Poster size will be 27 inches by 40 inches

Target Market(s)

Upper Middle class - movie lovers

Font styles to use
Sans Serif

Colors
33a6d7

Requirements
Must have
• NO CLIP ART - be original !
Nice to have
• abstract - think outside the box
Should not have
• CLIP ART

```html
<!DOCTYPE html>
<html lang="en">
<head>
<meta charset="utf-8">
<title>23rd Harrowgate Lantern Film Festival Poster</title>
<link href="https://fonts.googleapis.com/css2?family=Montserrat:wght@700&family=Oswald:wght@500&family=Poppins:wght@700&family=Gochi+Hand&display=swap" rel="stylesheet">
<style>
  :root {
    --page: #e9e6e3;
    --plum-light: #8a5a86;
    --plum-mid: #4a2a55;
    --plum-deep: #1c0d24;
    --ink-white: #ffffff;
    --logo-green: #8cc63f;
    --navy: #3a2f8a;
    --rose: #e8266f;
    --pink: #f3a0c8;
    --teal: #5fc8c0;
    --green: #26b04a;
    --orange: #f0742a;
    --magenta: #e0157f;
    --wine: #6b1232;
    --violet: #a35bb5;
    --coral: #ef6a4a;
    --sky: #33a6d7;
    --bokeh: rgba(150, 90, 170, 0.22);
  }
  * { margin: 0; padding: 0; box-sizing: border-box; }
  html, body { width: 1200px; height: 1200px; overflow: hidden; background: var(--page); }

  .poster {
    position: absolute;
    left: 221px; top: 19px;
    width: 757px; height: 1162px;
    background: linear-gradient(160deg, var(--plum-light) 0%, var(--plum-mid) 45%, var(--plum-deep) 100%);
    overflow: hidden;
  }
  .poster__panel {
    position: absolute;
    left: 44px; top: 68px;
    width: 665px; height: 1019px;
    background: linear-gradient(180deg, #452a58 0%, #2a1436 45%, #1a0b20 100%);
  }
  .poster__bokeh { position: absolute; inset: 0; }

  .brand {
    position: absolute;
    left: 0; right: 0; top: 120px;
    text-align: center;
    color: var(--ink-white);
  }
  .brand__dot {
    display: block;
    width: 44px; height: 44px;
    margin: 0 auto 8px;
    border-radius: 50%;
    background: var(--logo-green);
  }
  .brand__name {
    font-family: 'Montserrat', sans-serif;
    font-weight: 700;
    font-size: 52px;
    letter-spacing: 4px;
    line-height: 1;
  }
  .brand__rule {
    width: 202px; height: 2px;
    margin: 8px auto 6px;
    background: var(--logo-green);
  }
  .brand__sub {
    font-family: 'Oswald', sans-serif;
    font-weight: 500;
    font-size: 10.5px;
    letter-spacing: 0.3px;
  }

  .edition {
    position: absolute;
    left: 106px; top: 404px;
    font-family: 'Gochi Hand', cursive;
    color: var(--ink-white);
    font-size: 56px;
    line-height: 1;
  }
  .edition sup { font-size: 28px; vertical-align: 26px; margin-left: 4px; }

  .title {
    position: absolute;
    left: 0; right: 0; top: 474px;
    text-align: center;
    font-family: 'Poppins', sans-serif;
    font-weight: 700;
    font-size: 78px;
    line-height: 1;
    letter-spacing: 1px;
  }
  .title span:nth-child(1) { color: var(--navy); }
  .title span:nth-child(2) { color: var(--rose); }
  .title span:nth-child(3) { color: var(--pink); }
  .title span:nth-child(4) { color: var(--green); }
  .title span:nth-child(5) { color: var(--sky); }
  .title span:nth-child(6) { color: var(--magenta); }
  .title span:nth-child(7) { color: var(--orange); }
  .title span:nth-child(8) { color: var(--wine); }
  .title span:nth-child(9) { color: var(--violet); }
  .title span:nth-child(10) { color: var(--coral); }

  .subtitle {
    position: absolute;
    left: 0; right: 0; top: 552px;
    text-align: center;
    font-family: 'Gochi Hand', cursive;
    color: var(--ink-white);
    font-size: 46px;
    letter-spacing: 2px;
    line-height: 1;
  }

  .dates {
    position: absolute;
    left: 0; right: 0; top: 736px;
    text-align: center;
    font-family: 'Gochi Hand', cursive;
    color: var(--ink-white);
    font-size: 62px;
    line-height: 64px;
    letter-spacing: 2px;
  }
</style>
</head>
<body>
  <main class="poster">
    <svg class="poster__bokeh" width="757" height="1162" viewBox="0 0 757 1162" aria-hidden="true">
      <circle cx="380" cy="50" r="105" fill="rgba(180,120,170,0.25)"/>
      <circle cx="53" cy="355" r="55" fill="rgba(220,130,180,0.35)"/>
      <circle cx="10" cy="355" r="40" fill="rgba(230,150,190,0.25)"/>
    </svg>
    <div class="poster__panel"></div>
    <svg class="poster__bokeh" width="757" height="1162" viewBox="0 0 757 1162" aria-hidden="true">
      <circle cx="190" cy="119" r="22" fill="var(--bokeh)"/>
      <circle cx="201" cy="188" r="18" fill="var(--bokeh)"/>
      <circle cx="582" cy="206" r="54" fill="var(--bokeh)"/>
      <circle cx="533" cy="303" r="22" fill="rgba(120,70,160,0.35)"/>
      <circle cx="655" cy="82" r="18" fill="rgba(120,70,160,0.35)"/>
      <circle cx="529" cy="435" r="80" fill="rgba(90,40,110,0.3)"/>
      <circle cx="720" cy="602" r="22" fill="rgba(200,160,210,0.45)"/>
      <circle cx="192" cy="612" r="18" fill="var(--bokeh)"/>
      <circle cx="101" cy="688" r="32" fill="var(--bokeh)"/>
      <circle cx="297" cy="800" r="82" fill="rgba(90,40,110,0.25)"/>
      <circle cx="565" cy="820" r="18" fill="rgba(120,70,160,0.4)"/>
      <circle cx="379" cy="1102" r="52" fill="rgba(90,40,110,0.35)"/>
      <circle cx="191" cy="1031" r="22" fill="var(--bokeh)"/>
      <circle cx="735" cy="675" r="100" fill="rgba(90,40,110,0.2)"/>
    </svg>

    <header class="brand">
      <span class="brand__dot"></span>
      <div class="brand__name">HLFF</div>
      <div class="brand__rule"></div>
      <div class="brand__sub">HARROWGATE LANTERN FILM FESTIVAL</div>
    </header>

    <div class="edition">23<sup>RD</sup></div>

    <h1 class="title" aria-label="Harrowgate"><span>H</span><span>A</span><span>R</span><span>R</span><span>O</span><span>W</span><span>G</span><span>A</span><span>T</span><span>E</span></h1>
    <p class="subtitle">LANTERN FILM FESTIVAL</p>

    <p class="dates">21-29<br>AUGUST<br>2020</p>
  </main>
</body>
</html>
```